Business Cards for a law firm

Business cards for our law firm. Use our silhoette logo and OAK HARBOR - check our website (www.oakharbor-legal.com)

Contact Information for Business Card

our silhouette logo, OAK HARBOR, 800-555-0147, Dorian Kestrup, dorian@oakharbor-legal.com

Requirements
Must have
• our silhouette logo, OAK HARBOR, 800-555-0147, Dorian Kestrup, dorian@oakharbor-legal.com

```html
<!DOCTYPE html>
<html lang="en">
<head>
<meta charset="utf-8">
<title>Oak Harbor – Business Cards</title>
<link rel="stylesheet" href="https://fonts.googleapis.com/css2?family=Cinzel:wght@700&family=Montserrat:wght@700&family=Arimo:ital@1&display=swap">
<style>
  :root {
    --backdrop: #fcc113;
    --card-navy: #1a3169;
    --ink-deep: #071659;
    --mark-deep: #0d1c5e;
    --paper: #ffffff;
  }
  * { margin: 0; padding: 0; box-sizing: border-box; }
  html, body { width: 1200px; height: 1200px; overflow: hidden; }
  body { background: var(--backdrop); position: relative; }

  .card {
    position: absolute;
    left: 218px;
    width: 789px;
    height: 451px;
    background: var(--card-navy);
    box-shadow: 8px 8px 8px rgba(60, 40, 0, 0.55);
    overflow: hidden;
  }
  .card--front { top: 129px; }
  .card--back { top: 620px; }

  .brand-mark {
    position: absolute;
    background: var(--mark-deep);
  }
  .card--front .brand-mark { left: 40px; top: 120px; width: 200px; height: 200px; }
  .card--back .brand-mark { left: 44px; top: 52px; width: 86px; height: 86px; background: var(--paper); }

  .wordmark { position: absolute; font-family: "Cinzel", serif; font-weight: 700; white-space: nowrap; }
  .card--front .wordmark--top {
    left: 0; right: 0; padding-left: 290px; top: 140px;
    font-size: 96px; line-height: 1; color: var(--ink-deep); text-align: center; padding-right: 40px;
  }
  .card--front .wordmark--bottom {
    left: 0; right: 0; padding-left: 290px; top: 250px;
    font-size: 44px; line-height: 1; letter-spacing: 3px; color: var(--ink-deep); text-align: center; padding-right: 40px;
  }
  .card--back .wordmark {
    left: 170px; top: 84px; font-size: 46px; line-height: 1; letter-spacing: 2px; color: var(--paper);
  }

  .website {
    position: absolute; left: 0; right: 0; text-align: center;
    font-family: "Arimo", Arial, sans-serif; font-style: italic; font-size: 19px;
  }
  .card--front .website { top: 420px; color: var(--ink-deep); }
  .card--back .website { top: 405px; color: var(--paper); padding-right: 80px; }

  .holder {
    position: absolute; left: 31px; top: 193px;
    font-family: "Montserrat", sans-serif; font-weight: 700; font-size: 21px; letter-spacing: 0.5px;
    color: var(--paper);
  }
  .holder-rule {
    position: absolute; left: 293px; width: 467px; top: 206px; height: 1px; background: var(--paper);
  }

  .contact {
    position: absolute; left: 31px; display: flex; align-items: center; gap: 12px;
    font-family: "Arimo", Arial, sans-serif; font-style: italic; font-size: 19px; color: var(--paper);
  }
  .contact svg { width: 28px; height: 26px; fill: var(--paper); }
  .contact--phone { top: 262px; }
  .contact--email { top: 302px; }

  .foot-band { position: absolute; left: 0; bottom: 0; width: 100%; height: 14px; }
</style>
</head>
<body>
  <section class="card card--front">
    <div class="brand-mark" role="img" aria-label="Oak Harbor logo mark"></div>
    <div class="wordmark wordmark--top">OAK</div>
    <div class="wordmark wordmark--bottom">HARBOR</div>
    <p class="website">www.oakharbor-legal.com</p>
  </section>

  <section class="card card--back">
    <div class="brand-mark" role="img" aria-label="Oak Harbor logo mark"></div>
    <div class="wordmark">OAK HARBOR</div>
    <p class="holder">DORIAN KESTRUP</p>
    <div class="holder-rule"></div>

    <p class="contact contact--phone">
      <svg viewBox="0 0 24 24" aria-hidden="true"><path d="M6.6 10.8a15.1 15.1 0 0 0 6.6 6.6l2.2-2.2a1 1 0 0 1 1-.25 11.4 11.4 0 0 0 3.6.57 1 1 0 0 1 1 1V20a1 1 0 0 1-1 1A17 17 0 0 1 3 4a1 1 0 0 1 1-1h3.5a1 1 0 0 1 1 1c0 1.25.2 2.45.57 3.57a1 1 0 0 1-.25 1z"/></svg>
      800-555-0147
    </p>
    <p class="contact contact--email">
      <svg viewBox="0 0 28 20" aria-hidden="true"><path d="M0 0h28v20H0z M2 2v.6l12 9 12-9V2z M2 5v13h24V5l-12 9z" fill-rule="evenodd"/></svg>
      dorian@oakharbor-legal.com
    </p>

    <p class="website">www.oakharbor-legal.com</p>

    <svg class="foot-band" viewBox="0 0 789 14" preserveAspectRatio="none" aria-hidden="true">
      <polygon points="0,0 311,0 322,14 0,14" fill="#ffffff"/>
      <polygon points="327,0 789,0 789,14 338,14" fill="#ffffff"/>
    </svg>
  </section>
</body>
</html>
```